engineering and fabrication company- KelnoMarch

We require a full functional and coded website design for an engineering and fabrication company in Western Australia.
I have attached capability statement with a content of this website.
I would like to have Fabrication services divided into two sections

1. Steel Fabrication
2. Plastic Fabrication

Industry/Entity Type

mining , waste water , oil and gas , engineering and design

Coding

Coded - Design and coding required

Number of Pages Required

5+ page

Colors
0054AA
0677BA
7BADD7
CADEEF
E8F1F8
0094D4
00A9DD
6FCCEA
C7EBF8
E9F6FB

Requirements
Must have
• Must look very professional

```html
<!DOCTYPE html>
<html lang="en">
<head>
<meta charset="utf-8">
<title>KelnoMarch – Design / Engineering / Fabrication</title>
<link href="https://fonts.googleapis.com/css2?family=Roboto:wght@400;500;700&family=Arimo:wght@400;700&display=swap" rel="stylesheet">
<style>
:root{
  --navy:#0054AA;
  --blue:#0677BA;
  --sky:#0094D4;
  --cyan:#1BA6E0;
  --pale:#E9F6FB;
  --ink:#222;
  --text:#555;
  --grey-bg:#f5f5f5;
  --white:#fff;
}
*{margin:0;padding:0;box-sizing:border-box}
html,body{width:1200px;height:3837px;overflow:hidden}
body{position:relative;font-family:"Arimo",Arial,sans-serif;color:var(--text);background:var(--white)}
.abs{position:absolute}
.head-font{font-family:"Roboto",Arial,sans-serif}

/* header */
.topline{left:0;top:0;width:1200px;height:6px;background:var(--cyan)}
.header{left:0;top:6px;width:1200px;height:128px;background:var(--white);border-bottom:1px solid #e4e4e4}
.brand{left:112px;top:14px;display:flex;align-items:center;gap:10px}
.brand-mark{width:18px;height:18px;background:var(--sky)}
.brand-name{font-family:"Roboto",sans-serif;font-weight:700;font-size:30px;color:var(--sky)}
.brand-tag{left:112px;top:60px;font-size:11px;color:#777;letter-spacing:.3px}
.contact-item{display:flex;align-items:center;gap:12px;top:22px}
.contact-icon{width:40px;height:40px;border:1.5px solid var(--sky);border-radius:50%;display:flex;align-items:center;justify-content:center}
.contact-label{font-family:"Roboto",sans-serif;font-size:13px;color:#888}
.contact-value{font-family:"Roboto",sans-serif;font-weight:500;font-size:17px;color:var(--ink)}
.nav{top:96px;right:112px;display:flex;gap:50px;font-family:"Roboto",sans-serif;font-weight:500;font-size:14px;color:#333}
.nav .active{color:var(--navy)}

/* hero */
.hero{left:0;top:135px;width:1200px;height:724px;background:linear-gradient(100deg,#1c2a30 0%,#2c4a52 35%,#1a3c44 60%,#3a4a3a 85%,#5a4a20 100%)}
.hero-title{left:596px;top:390px;font-family:"Roboto",sans-serif;font-weight:500;font-size:76px;letter-spacing:2px;color:var(--white)}
.hero-sub{left:597px;top:480px;font-family:"Roboto",sans-serif;font-size:27px;color:var(--white)}
.hero-btn{left:601px;top:540px;width:176px;height:57px;border:2px solid var(--white);border-radius:30px;color:var(--white);font-family:"Roboto",sans-serif;font-weight:500;font-size:17px;display:flex;align-items:center;justify-content:center}
.dots{left:575px;top:824px;display:flex;gap:7px}
.dots span{width:12px;height:12px;border-radius:50%;background:var(--white)}
.dots span.on{background:var(--sky)}

/* capability */
.capability{left:0;top:859px;width:1200px;height:648px;background:var(--grey-bg);text-align:center}
.section-title{font-family:"Roboto",sans-serif;font-size:35px;color:var(--ink);width:100%;text-align:center}
.cap-title{top:56px}
.cap-lead{top:108px;width:100%;font-family:"Roboto",sans-serif;font-size:19px;line-height:30px;color:var(--sky)}
.cap-body{left:210px;width:780px;font-size:13.5px;line-height:26.5px;color:#555}
.btn-solid{left:500px;top:505px;width:200px;height:58px;border-radius:30px;background:var(--navy);color:var(--white);font-family:"Roboto",sans-serif;font-weight:500;font-size:19px;display:flex;align-items:center;justify-content:center}

/* services */
.underline{height:3px;width:48px;background:var(--navy)}
.service-cell{width:488px;height:359px}
.photo-steel{background:linear-gradient(135deg,#6c6c68 0%,#4a4a48 45%,#8a8678 100%)}
.photo-plastic{background:linear-gradient(135deg,#8a8d90 0%,#2a5aa8 45%,#1c3f8a 70%,#7c8088 100%)}
.service-text{background:var(--grey-bg);padding:40px 40px}
.service-title{font-family:"Roboto",sans-serif;font-weight:500;font-size:25px;color:var(--navy)}
.service-body{font-size:13px;line-height:25.7px;color:#666;margin-top:28px;text-align:justify}
.btn-outline{width:140px;height:48px;border:2px solid var(--navy);border-radius:26px;color:var(--navy);font-family:"Roboto",sans-serif;font-weight:500;font-size:15px;display:flex;align-items:center;justify-content:center;margin-top:24px}

/* testimonials */
.testimonials{left:0;top:2452px;width:1200px;height:407px;background:var(--cyan);color:var(--white);text-align:center}
.quote{left:270px;width:660px;top:141px;font-size:13.5px;line-height:25.7px}
.person{top:295px;width:100%;font-family:"Roboto",sans-serif;font-weight:500;font-size:21px}
.person-role{top:330px;width:100%;font-size:14px}

/* blog */
.card{width:311px;top:2987px}
.card-photo{height:244px}
.blog-a{background:linear-gradient(135deg,#9aa0a8,#3a5a9a 45%,#c8b030 75%,#8a9096)}
.blog-b{background:linear-gradient(135deg,#101418,#1a1e24 40%,#f0d020 55%,#e8c818 75%,#14181c)}
.blog-c{background:linear-gradient(180deg,#b8b4a8,#6a6c6c 50%,#8a8478)}
.card-body{margin:-18px 16px 0;background:var(--white);position:relative;text-align:center;padding-top:14px}
.card-date{font-family:"Roboto",sans-serif;font-weight:500;font-size:19px;color:var(--navy)}
.card-title{font-family:"Roboto",sans-serif;font-weight:500;font-size:12.5px;color:#333;margin-top:14px}
.card-text{font-size:13px;line-height:24px;color:#666;margin-top:8px}

/* footer */
.footer{left:0;top:3410px;width:1200px;height:427px;background:var(--navy);color:var(--white)}
.foot-brand{top:26px;width:100%;text-align:center;font-family:"Roboto",sans-serif;font-weight:700;font-size:32px}
.foot-tag{top:78px;width:100%;text-align:center;font-size:11px;color:#b9d2ee}
.foot-nav{top:202px;width:100%;display:flex;justify-content:center;gap:50px;font-family:"Roboto",sans-serif;font-weight:500;font-size:14px}
.foot-contact{display:flex;align-items:center;gap:18px;font-family:"Roboto",sans-serif;font-size:15.5px;line-height:24px}
.ring{width:44px;height:44px;border:1.5px solid var(--white);border-radius:50%;display:flex;align-items:center;justify-content:center;flex:none}
.social{top:368px;left:110px;display:flex;gap:8px}
.social span{width:40px;height:40px;border:2px solid var(--white);border-radius:50%}
.copyright{top:378px;right:112px;font-size:15px}
</style>
</head>
<body>

<div class="abs topline"></div>
<header class="abs header">
  <div class="abs brand"><span class="brand-mark"></span><span class="brand-name">KelnoMarch</span></div>
  <div class="abs brand-tag">Design / Engineering / Fabrication</div>

  <div class="abs contact-item" style="left:647px">
    <div class="contact-icon">
      <svg width="18" height="18" viewBox="0 0 24 24"><path d="M6.6 10.8a15.1 15.1 0 0 0 6.6 6.6l2.2-2.2c.3-.3.7-.4 1-.2 1.1.4 2.3.6 3.6.6.6 0 1 .4 1 1V20c0 .6-.4 1-1 1A17 17 0 0 1 3 4c0-.6.4-1 1-1h3.5c.6 0 1 .4 1 1 0 1.3.2 2.5.6 3.6.1.3 0 .7-.2 1z" fill="#0094D4"/></svg>
    </div>
    <div><div class="contact-label">Call Us</div><div class="contact-value">+1 555 010 2040</div></div>
  </div>
  <div class="abs contact-item" style="left:882px">
    <div class="contact-icon">
      <svg width="20" height="16" viewBox="0 0 20 16"><rect x="1" y="1" width="18" height="14" rx="1.5" fill="none" stroke="#0094D4" stroke-width="1.5"/><path d="M1.5 2l8.5 7 8.5-7" fill="none" stroke="#0094D4" stroke-width="1.5"/></svg>
    </div>
    <div><div class="contact-label">Email</div><div class="contact-value">info@kelnomarch.com</div></div>
  </div>

  <nav class="abs nav">
    <span class="active">HOME</span><span>ABOUT US</span><span>MISSION</span><span>SERVICES</span><span>NEWS</span><span>CONTACT US</span>
  </nav>
</header>

<section class="abs hero" role="img" aria-label="Engineer in a hard hat working at a digital control screen beside robotic arms in a factory">
</section>
<h1 class="abs hero-title">KELNOMARCH</h1>
<div class="abs hero-sub">DESIGN /ENGINEERING / FABRICATION</div>
<div class="abs hero-btn">LEARN MORE</div>
<div class="abs dots"><span></span><span class="on"></span><span></span></div>

<section class="abs capability">
  <h2 class="abs section-title cap-title">CAPABILITY STATEMENT</h2>
  <p class="abs cap-lead">KelnoMarch, is a multi-disciplinary design/engineering and fabrication<br>company based in Harlow Park , Western Australia</p>
  <p class="abs cap-body" style="top:184px">The guiding force in all that we do is our commitment to providing hands-on reliable customer service and quality metal and plastic components for a broad range of industries including Mining, Chemical Industry, Oil and Gas , Water Treatment, Agricultural Equipment, Material Handling, Construction Equipment, Renewable Energy &amp; more.</p>
  <p class="abs cap-body" style="top:290px">At our Harlow Park location, you will find a team of experienced manufacturing professionals ready to provide value-added services including integrated project management, new product development, engineering collaboration, fabrication, welding and finishing. We have the machinery and the expertise to provide highly integrated, comprehensive manufacturing solutions.</p>
  <p class="abs cap-body" style="top:397px">With over 100 years of our combined experience and years of service in Metal and Plastic fabrication shops as well as design offices , we are grateful to our customers who helped us get here. That gratitude is reflected in the work we do and it's what drives us forward each day. We are proud of who we are and excited to share our future.</p>
  <div class="abs btn-solid">READ MORE</div>
</section>

<h2 class="abs section-title" style="top:1555px">FABRICATION SERVICES</h2>
<div class="abs underline" style="left:576px;top:1606px"></div>

<div class="abs service-cell photo-steel" style="left:112px;top:1654px" role="img" aria-label="Large welded steel pipe spool with flanged ends in a workshop"></div>
<div class="abs service-cell service-text" style="left:600px;top:1654px">
  <h3 class="service-title">STEEL FABRICATION</h3>
  <div class="underline" style="margin-top:12px;width:54px"></div>
  <p class="service-body">KelnoMarch steel division manufactures in house a vast array of steel pipe components for our own pipeline applications or for external sale. From butt weld or flanged pipe fittings in equal and reduced tee's, reducers, bends, all components are made and tested to your specifications and can include final coatings such as paint, hot dip galvanising, epoxy, or powder coating.</p>
  <div class="btn-outline">READ MORE</div>
</div>
<div class="abs service-cell service-text" style="left:112px;top:2013px">
  <h3 class="service-title">PLASTIC FABRICATION</h3>
  <div class="underline" style="margin-top:12px;width:54px"></div>
  <p class="service-body">KelnoMarch manufactures a range of pipe spools to customer's requirements. Spools can be manufactured in most thermoplastics including PE, PP, PVDF, ECTFE and PVC. Material choice is dependent on operating conditions &amp; customer requirements. KelnoMarch manufactures a range of pipe spools to customer's requirements.Spools can be manufactured....</p>
  <div class="btn-outline">READ MORE</div>
</div>
<div class="abs service-cell photo-plastic" style="left:600px;top:2013px" role="img" aria-label="Blue butt fusion welding machine clamping black plastic pipe"></div>

<section class="abs testimonials">
  <h2 class="abs section-title" style="top:58px;color:#fff">OUR TESTIMONIALS</h2>
  <p class="abs quote"><svg width="24" height="18" viewBox="0 0 24 18" style="vertical-align:-3px;margin-right:6px"><path d="M0 18V10C0 4 3 1 9 0v4C6 5 5 7 5 9h4v9zM13 18V10c0-6 3-9 9-10v4c-3 1-4 3-4 5h4v9z" fill="#fff"/></svg>Sed ut perspiciatis unde omnis iste natus error sit voluptatem accusantium doloremque laudantium, totam rem aperiam, eaque ipsa quae ab illo inventore veritatis et quasi architecto beatae vitae dicta sunt explicab Nemo enim ipsam voluptatem quia voluptas sit aspernatur aut odit aut fugit, sed quia consequuntur magni error sit voluptatem accusantium doloremque laudantiumerror sit voluptatem accusantium doloremque laud antium dolores eos qui ratione voluptatem sequi nesciunt.<svg width="24" height="18" viewBox="0 0 24 18" style="vertical-align:-8px;margin-left:6px"><path d="M24 0v8c0 6-3 9-9 10v-4c3-1 4-3 4-5h-4V0zM11 0v8c0 6-3 9-9 10v-4c3-1 4-3 4-5H2V0z" fill="#fff"/></svg></p>
  <div class="abs person">-Dara Quill</div>
  <div class="abs person-role">Sed ut perspiciatis unde omnis iste</div>
</section>

<h2 class="abs section-title" style="top:2905px">LATEST BLOG</h2>
<div class="abs underline" style="left:576px;top:2956px"></div>

<article class="abs card" style="left:112px">
  <div class="card-photo blog-a" role="img" aria-label="Industrial pump assembly with blue motor and yellow frame"></div>
  <div class="card-body"><div class="card-date">DEC 03,2022</div><div class="card-title">SED UT PERSPICIATIS UNDE OMNIS</div><p class="card-text">Nemo enim ipsam voluptatem quia vol<br>uptas sit aspernatur aut odit aut fugit,<br>dolores eos qui ratione</p></div>
</article>
<article class="abs card" style="left:445px">
  <div class="card-photo blog-b" role="img" aria-label="Yellow fabricated plastic housing parts on a dark background"></div>
  <div class="card-body"><div class="card-date">DEC 03,2022</div><div class="card-title">SED UT PERSPICIATIS UNDE OMNIS</div><p class="card-text">Nemo enim ipsam voluptatem quia vol<br>uptas sit aspernatur aut odit aut fugit,<br>dolores eos qui ratione</p></div>
</article>
<article class="abs card" style="left:779px">
  <div class="card-photo blog-c" role="img" aria-label="Rows of galvanised valve assemblies laid out on a gravel yard"></div>
  <div class="card-body"><div class="card-date">DEC 03,2022</div><div class="card-title">SED UT PERSPICIATIS UNDE OMNIS</div><p class="card-text">Nemo enim ipsam voluptatem quia vol<br>uptas sit aspernatur aut odit aut fugit,<br>dolores eos qui ratione</p></div>
</article>

<footer class="abs footer">
  <div class="abs foot-brand">KelnoMarch</div>
  <div class="abs foot-tag">Design / Engineering / Fabrication</div>
  <nav class="abs foot-nav"><span>HOME</span><span>ABOUT US</span><span>MISSION</span><span>SERVICES</span><span>NEWS</span><span>CONTACT US</span></nav>

  <div class="abs foot-contact" style="left:151px;top:268px">
    <div class="ring"><svg width="14" height="20" viewBox="0 0 14 20"><path d="M7 0a7 7 0 0 0-7 7c0 5 7 13 7 13s7-8 7-13a7 7 0 0 0-7-7zm0 9.5A2.5 2.5 0 1 1 7 4.5a2.5 2.5 0 0 1 0 5z" fill="#fff"/></svg></div>
    <div>265 Lorem Ipsum Dummy lorem<br>Lorem Ipsum</div>
  </div>
  <div class="abs foot-contact" style="left:545px;top:268px">
    <div class="ring"><svg width="18" height="18" viewBox="0 0 24 24"><path d="M6.6 10.8a15.1 15.1 0 0 0 6.6 6.6l2.2-2.2c.3-.3.7-.4 1-.2 1.1.4 2.3.6 3.6.6.6 0 1 .4 1 1V20c0 .6-.4 1-1 1A17 17 0 0 1 3 4c0-.6.4-1 1-1h3.5c.6 0 1 .4 1 1 0 1.3.2 2.5.6 3.6.1.3 0 .7-.2 1z" fill="#fff"/></svg></div>
    <div>+1 555 010 2040</div>
  </div>
  <div class="abs foot-contact" style="left:836px;top:268px">
    <div class="ring"><svg width="18" height="14" viewBox="0 0 20 16"><rect x="0" y="0" width="20" height="16" rx="2" fill="#fff"/><path d="M1 1.5l9 7 9-7" fill="none" stroke="#0054AA" stroke-width="1.6"/></svg></div>
    <div>info@kelnomarch.com</div>
  </div>

  <div class="abs social"><span></span><span></span><span></span></div>
  <div class="abs copyright">© 2022 KelnoMarch.All rights reserved</div>
</footer>

</body>
</html>
```